varnok llc

excavating and landscaping

Target Market(s)

Industry/Entity Type

Contact Information for Business Card

file atach

Font styles to use
Serif

```html
<!DOCTYPE html>
<html lang="en">
<head>
<meta charset="utf-8">
<title>Varnok LLC – Business Card</title>
<link rel="stylesheet" href="https://fonts.googleapis.com/css2?family=Roboto:wght@400;500;700&display=swap">
<style>
  :root {
    --page: #ffffff;
    --ink: #000000;
    --paper: #ffffff;
    --red: #d40000;
    --text-dark: #1c1c1c;
    --text-mid: #333333;
    --shadow: rgba(0, 0, 0, 0.28);
  }
  * { margin: 0; padding: 0; box-sizing: border-box; }
  html, body {
    width: 687px;
    height: 1200px;
    overflow: hidden;
    background: var(--page);
    font-family: "Roboto", Arial, sans-serif;
  }
  .sheet {
    position: relative;
    width: 687px;
    height: 1200px;
    display: flex;
    flex-direction: column;
    align-items: center;
    justify-content: center;
    gap: 44px;
  }
  .card {
    display: block;
    width: 600px;
    height: 343px;
    box-shadow: 0 3px 10px var(--shadow);
  }
  .card text { font-family: "Roboto", Arial, sans-serif; }
  .fill-ink { fill: var(--ink); }
  .fill-paper { fill: var(--paper); }
  .fill-red { fill: var(--red); }
  .brand-name { fill: var(--paper); font-weight: 700; }
  .web-white { fill: var(--paper); font-weight: 700; }
  .web-red { fill: var(--red); font-weight: 700; }
  .holder-name { fill: var(--text-dark); font-weight: 500; }
  .holder-role { fill: var(--text-mid); font-weight: 400; }
  .contact-line { fill: var(--text-dark); font-weight: 500; }
  .tagline { fill: var(--paper); font-weight: 500; }
  .back-web { fill: var(--red); font-weight: 500; }
</style>
</head>
<body>
<main class="sheet">

  <!-- Front of card -->
  <svg class="card card-front" viewBox="0 0 944 540" role="group" aria-label="Business card front">
    <rect class="fill-ink" width="944" height="540"/>
    <text class="brand-name" x="472" y="340" text-anchor="middle" font-size="78" letter-spacing="2">VARNOK LLC</text>
    <rect class="fill-red" x="0" y="436" width="258" height="4"/>
    <rect class="fill-red" x="686" y="436" width="258" height="4"/>
    <text x="472" y="448" text-anchor="middle" font-size="28" letter-spacing="0.5"><tspan class="web-white">www.</tspan><tspan class="web-red">varnokllc</tspan><tspan class="web-white">.com</tspan></text>
  </svg>

  <!-- Back of card -->
  <svg class="card card-back" viewBox="0 0 944 540" role="group" aria-label="Business card back">
    <rect class="fill-paper" width="944" height="540"/>
    <path class="fill-ink" d="M564 0 C518 110 470 330 464 540 L944 540 L944 0 Z"/>
    <path class="fill-red" d="M563 60 C528 200 490 400 486 540 L520 540 C522 400 540 240 563 60 Z"/>

    <rect class="fill-ink" x="0" y="97" width="23" height="65"/>
    <rect class="fill-red" x="23" y="97" width="33" height="65"/>
    <text class="holder-name" x="99" y="126" font-size="35">DAN MERROW</text>
    <text class="holder-role" x="99" y="161" font-size="24">OWNER</text>

    <g class="contact-icons">
      <path class="fill-red" d="M58 293 l5 -3 l5 6 l-3 3 c2 4 5 7 9 9 l3 -3 l6 5 l-3 5 c-12 -1 -21 -10 -22 -22 Z"/>
      <path class="fill-red" d="M58 327 l5 -3 l5 6 l-3 3 c2 4 5 7 9 9 l3 -3 l6 5 l-3 5 c-12 -1 -21 -10 -22 -22 Z"/>
      <path class="fill-red" fill-rule="evenodd" d="M69 373 c-6 0 -11 5 -11 11 c0 8 11 18 11 18 c0 0 11 -10 11 -18 c0 -6 -5 -11 -11 -11 Z M69 380 a4 4 0 1 0 0.1 0 Z"/>
      <path class="fill-red" d="M55 406 q14 4 28 0 l0 2 q-14 5 -28 0 Z"/>
      <rect class="fill-red" x="56" y="426" width="26" height="18" rx="2"/>
      <path d="M57 428 L69 437 L81 428" fill="none" stroke="#ffffff" stroke-width="2"/>
    </g>
    <g class="contact-lines" font-size="24">
      <text class="contact-line" x="98" y="313">555 0142 318</text>
      <text class="contact-line" x="98" y="347">555 0142 318</text>
      <text class="contact-line" x="98" y="382">P.O Box 2218 Elmvale</text>
      <text class="contact-line" x="98" y="411">Centre Qld 4109</text>
      <text class="contact-line" x="98" y="448">info@varnokllc.com</text>
    </g>

    <text class="tagline" x="636" y="84" font-size="30">EXCAVATING &amp;</text>
    <text class="tagline" x="636" y="113" font-size="23" letter-spacing="4.5">LANDSCAPING</text>

    <text class="brand-name" x="738" y="338" text-anchor="middle" font-size="44" letter-spacing="1">VARNOK LLC</text>

    <text class="back-web" x="732" y="478" text-anchor="middle" font-size="22" letter-spacing="2">www.varnokllc.com</text>
  </svg>

</main>
</body>
</html>
```